Financial Planning Business needs a business card design

We need a business card design that is for a new financial planning business based in Australia. We provide financial planning advice such as retirement planning, wealth creation, asset protection.

Attached is the logo design. On the front side of the business card needs to incorporate the following:
- adviser name
- adviser title (ie Managing Director)
- address
- phone number
- email
- website address

Ideally it should also have the business name and logo

On the back of the card I would like this to be black in colour with the business name and logo

I have been advised the font is "Cinzel" (regular and bold)

Industry/Entity Type

Financial

Requirements
Must have
• Logo and business name

Format to have as follows:
Ben xxxxxxxx
Managing Director / Senior Financial Adviser
address
phone email
website

```html
<!DOCTYPE html>
<html lang="en">
<head>
<meta charset="utf-8">
<title>Harbourline Wealth Planning – Business Card</title>
<link rel="stylesheet" href="https://fonts.googleapis.com/css2?family=Cinzel:wght@400;700&family=Open+Sans:wght@400;600&display=swap">
<style>
  :root {
    --stage: #ececec;
    --paper: #ffffff;
    --ink-dark: #121314;
    --ink-mid: #23262a;
    --accent: #1a9ad6;
    --silver: #b9bcc0;
    --divider: #8a8d91;
    --text-light: #f2f2f2;
    --brand-grey: #8c8c8c;
  }
  * { box-sizing: border-box; margin: 0; padding: 0; }
  html, body { width: 1200px; height: 900px; overflow: hidden; }
  body {
    background: var(--stage);
    display: flex;
    align-items: center;
    justify-content: center;
    gap: 40px;
  }
  .card {
    width: 540px;
    height: 310px;
    border-radius: 20px;
    overflow: hidden;
    position: relative;
    box-shadow: 0 10px 24px rgba(0,0,0,0.18);
  }

  /* Brand lockup */
  .brand {
    display: flex;
    align-items: center;
    gap: 16px;
  }
  .brand-square {
    width: 58px;
    height: 58px;
    background: var(--accent);
    flex: none;
  }
  .brand-name {
    font-family: "Cinzel", serif;
    font-weight: 700;
    color: var(--accent);
    line-height: 1.05;
  }
  .brand-name .line-main { display: block; font-size: 40px; }
  .brand-name .line-sub { display: block; font-size: 19px; letter-spacing: 0.5px; }

  /* Front */
  .card-front { background: var(--paper); }
  .front-top {
    height: 138px;
    display: flex;
    align-items: center;
    padding-left: 60px;
  }
  .front-rule {
    height: 10px;
    background: var(--accent);
    border-bottom: 4px solid var(--silver);
  }
  .front-bottom {
    height: 162px;
    background: linear-gradient(180deg, var(--ink-mid) 0%, var(--ink-dark) 100%);
    display: flex;
    align-items: center;
    padding: 0 30px;
  }
  .person {
    width: 170px;
    text-align: right;
    padding-right: 16px;
    font-family: "Open Sans", sans-serif;
    align-self: flex-start;
    margin-top: 20px;
  }
  .person-name { color: var(--accent); font-weight: 600; font-size: 17px; }
  .person-title { color: var(--text-light); font-size: 12px; margin-top: 2px; }
  .divider {
    width: 1px;
    height: 96px;
    background: var(--divider);
  }
  .contacts {
    list-style: none;
    padding-left: 18px;
    font-family: "Open Sans", sans-serif;
    font-size: 15px;
    color: var(--text-light);
  }
  .contacts li {
    display: flex;
    align-items: center;
    gap: 8px;
    line-height: 26px;
  }
  .contacts svg { width: 14px; height: 14px; fill: var(--accent); flex: none; }

  /* Back */
  .card-back {
    background: radial-gradient(ellipse at 55% 45%, #2a2d31 0%, #16181a 55%, #0c0d0e 100%);
    display: flex;
    align-items: center;
    justify-content: center;
  }
</style>
</head>
<body>

<section class="card card-front" aria-label="Card front">
  <div class="front-top">
    <div class="brand">
      <span class="brand-square"></span>
      <span class="brand-name"><span class="line-main">Harbourline</span><span class="line-sub">Wealth Planning</span></span>
    </div>
  </div>
  <div class="front-rule"></div>
  <div class="front-bottom">
    <div class="person">
      <p class="person-name">Jordan Hale</p>
      <p class="person-title">Managing Director</p>
    </div>
    <div class="divider"></div>
    <ul class="contacts">
      <li><svg viewBox="0 0 16 16"><path d="M8 1 1 7.5h2V15h4v-4h2v4h4V7.5h2z"/></svg>PO Box 40517 NS 21094</li>
      <li><svg viewBox="0 0 16 16"><path d="M4 1.5 6.2 4 5 6c.8 2 2.6 3.8 4.6 4.6l2-1.2L14.5 12 13 14.5C7 14 2 9 1.5 3z"/></svg>1482 307 926</li>
      <li><svg viewBox="0 0 16 16"><path d="M1 4h14v9H1zM1 4l7 5 7-5" stroke="#1a9ad6" stroke-width="1" fill="none"/><path d="M2 5l6 4.3L14 5v7H2z"/></svg>jordan@harbourline.com</li>
      <li><svg viewBox="0 0 16 16"><circle cx="8" cy="8" r="6.5" fill="none" stroke="#1a9ad6" stroke-width="1.4"/><path d="M1.5 8h13M8 1.5c-3 3.5-3 9.5 0 13M8 1.5c3 3.5 3 9.5 0 13" fill="none" stroke="#1a9ad6" stroke-width="1.2"/></svg>www.harbourline.com</li>
    </ul>
  </div>
</section>

<section class="card card-back" aria-label="Card back">
  <div class="brand">
    <span class="brand-square"></span>
    <span class="brand-name"><span class="line-main">Harbourline</span><span class="line-sub">Wealth Planning</span></span>
  </div>
</section>

</body>
</html>
```